TQ27 Computer Produced for Poultry Houses needs a Corporate Touch

We need a unique screen design with unique graphics for our new product called "TQ27". TQ27 product is a computer produced for poultry houses. It has a LED screen on which user can change settings for heating, air quaility, inside temprateure, cooling, pressure etc as defined in the attached pictures.

We need 6 designs for the following :

1- TQ27 BOX Front Cover Design
2- LED Screen Main Menu
3- LED Screen Inner Menu
4- LED Screen Main Page Menu
5- Vector Logo (JPEG is included, will be prepared in vectorel format)
6- Stationery Design

Explanations are defined below:

1- TQ27 BOX Front Cover Design: This box is 37cm width and 47 cm height. It has a LED screen (19 cm x 14cm) in the middle and 3 circular buttons under the LED screen as seenin the attachment. We need a simple but good quality design including corporate colors (dark blue and red) for this box only for the front face of the box.

Attached pictures : 1-a.jpg 1-b.jpg 1-c.jpg (example)

2- LED Screen Main Menu : LED screen (8.7 cm x 15.5 cm) and a border. This menu includes 12 main menu buttons. You will design 12 menu buttons. This menu should look like panelix start menu or orbifon menu with icons.
a- Values
b- Air Conditioning
c- Heating
d- Alarm
e- Fans
f- Cooling
g-Pressure
h-Timing
i- Reports
j- Close Lights
k- Weights
l- Management (Admin)

Attached pictures : 2-a.jpg 2-b.jpg LEDDimensions.jpg

3- LED Screen Inner Menu : This screen is one example inner menu when clicked on one of icons defined in (2). You will design up and down arrows, textbox and "Go to back" button and "Go to Home" button and final screen design (placement)

Attached pictures : 3-a.jpg

4- LED Screen Main Page Menu : This menu has a poultry house drawing with summary information boxes above.

You will submit the main page design.

Additionally, We need 3 GIF pictures with animation (defined in 4-a.jpg)
a- Moving fans (turning)
b- Fire (burning)
c- Pets (dropping wet drops down on the pad - brown rectangular area)
Attached pictures : 4-a.jpg

Poultry house has 10 fans all in one row. and 6 fans on the long side.

5- Vector logo : In this part, you will submit 2 vectorel logos. First, you will design Vectorel format of velmora_logo.png (attached) and PNG format. And will design TQ27 logo with same structure, fonts, puntos.

6- Stationery Design : Cardvisit + Letter design + Company headed paper

Computer

0456a4
ef363c
add136

• Flat design, best user experience

```html
<!DOCTYPE html>
<html lang="tr">
<head>
<meta charset="UTF-8">
<title>TQ27 Front Cover</title>
<link href="https://fonts.googleapis.com/css2?family=Open+Sans:wght@400;600;700&display=swap" rel="stylesheet">
<style>
  :root{
    --face-light:#e4e4f2;
    --face-mid:#9fa4d6;
    --face-deep:#3f4ea6;
    --screen-blue:#2140a0;
    --screen-blue-light:#3354b4;
    --screen-line:#e9ecf7;
    --brand-blue:#1f2f8c;
    --brand-red:#ef363c;
    --knob:#141414;
    --go-green:#1fbf4a;
    --label:#2a3a8f;
  }
  html,body{margin:0;padding:0;width:949px;height:1200px;overflow:hidden;background:#f2f2f2;}
  body{font-family:"Open Sans",Arial,sans-serif;}
  .cover{
    position:relative;width:949px;height:1200px;overflow:hidden;
    background:
      radial-gradient(ellipse 620px 420px at 520px 920px, rgba(255,255,255,.75), rgba(255,255,255,0) 70%),
      radial-gradient(ellipse 520px 520px at 250px 300px, rgba(255,255,255,.35), rgba(255,255,255,0) 70%),
      linear-gradient(160deg, var(--face-mid) 0%, var(--face-deep) 40%, var(--face-mid) 70%, var(--face-light) 100%);
    border-radius:10px;
  }
  .screen{
    position:absolute;left:207px;top:276px;width:534px;height:393px;
    background:var(--screen-line);
    border:2px solid var(--screen-line);
    box-sizing:border-box;
    display:grid;
    grid-template-rows:55px 55px 1fr 55px;
    row-gap:3px;
  }
  .tile-row{display:grid;grid-template-columns:repeat(7,1fr);column-gap:3px;}
  .tile{
    background:var(--screen-blue);color:#fff;padding:2px 0 0 10px;
    display:flex;flex-direction:column;justify-content:center;
  }
  .tile .name{font-size:10px;font-weight:600;line-height:1.05;text-transform:uppercase;}
  .tile .value{font-size:15px;line-height:1.2;}
  .house{
    background:
      radial-gradient(ellipse 230px 90px at 290px 130px, var(--screen-blue-light), rgba(51,84,180,0) 75%),
      var(--screen-blue);
  }
  .status-row{display:grid;grid-template-columns:149px 150px 75px 76px 1fr;column-gap:3px;}
  .status{background:var(--screen-blue);color:#fff;display:flex;flex-direction:column;justify-content:center;padding-left:16px;}
  .status.center{align-items:center;padding-left:0;}
  .status .name{font-size:11.5px;font-weight:600;line-height:1.3;}
  .status .value{font-size:12px;line-height:1.3;}
  .status.menu{font-size:12.5px;font-weight:600;align-items:center;padding-left:0;}
  .control{position:absolute;top:830px;width:160px;margin-left:-80px;text-align:center;}
  .control .label{font-size:14px;font-weight:600;color:var(--label);letter-spacing:.3px;}
  .control svg{display:block;margin:10px auto 0;}
  .brand{
    position:absolute;left:99px;top:1028px;display:flex;align-items:flex-start;gap:14px;
  }
  .brand .mark{width:52px;height:58px;background:var(--brand-blue);}
  .brand .name{font-size:40px;font-weight:700;color:var(--brand-blue);letter-spacing:-1px;line-height:46px;}
  .brand-line{
    position:absolute;left:151px;right:0;top:1078px;height:8px;
    background:linear-gradient(90deg,var(--brand-red) 0%,var(--brand-red) 40%,rgba(239,54,60,.25) 100%);
  }
</style>
</head>
<body>
<div class="cover">
  <div class="screen">
    <div class="tile-row">
      <div class="tile"><span class="name">Isı Set</span><span class="value">0.0</span></div>
      <div class="tile"><span class="name">Ön Isı</span><span class="value">0.0</span></div>
      <div class="tile"><span class="name">Arka Isı</span><span class="value">0.0</span></div>
      <div class="tile"><span class="name">Ort. Isı</span><span class="value">0.0</span></div>
      <div class="tile"><span class="name">Dış Isı</span><span class="value">0.0</span></div>
      <div class="tile"><span class="name">Ön Hava<br>Kalite</span><span class="value">0.0</span></div>
      <div class="tile"><span class="name">Ort. Hava<br>Kalite</span><span class="value">0.0</span></div>
    </div>
    <div class="tile-row">
      <div class="tile"><span class="name">Nem Set</span><span class="value">0.0</span></div>
      <div class="tile"><span class="name">Ön Nem</span><span class="value">0.0</span></div>
      <div class="tile"><span class="name">Arka Nem</span><span class="value">0.0</span></div>
      <div class="tile"><span class="name">Ort. Nem</span><span class="value">0.0</span></div>
      <div class="tile"><span class="name">Dış Nem</span><span class="value">0.0</span></div>
      <div class="tile"><span class="name">Arka Hava<br>Kalite</span><span class="value">0.0</span></div>
      <div class="tile"><span class="name">Süronon<br>Yaşı</span><span class="value">0.0</span></div>
    </div>
    <div class="house" role="img" aria-label="Line drawing of the poultry house with silo, air inlets and labelled fans MF1–MF5 and TF1–TF10"></div>
    <div class="status-row">
      <div class="status center"><span class="name">KLAPE %</span><span class="value">0,0</span></div>
      <div class="status center"><span class="name">PERDE %</span><span class="value">0,0</span></div>
      <div class="status"><span class="name">PA</span><span class="value">0,0</span></div>
      <div class="status center" aria-label="Heating">
        <svg width="20" height="28" viewBox="0 0 22 30"><path d="M11 2 C13 8 20 12 19 20 C18 26 14 28 11 28 C7 28 3 25 3 20 C3 15 7 13 8 8 C10 11 10 13 12 14 C13 10 12 6 11 2 Z" fill="none" stroke="#fff" stroke-width="2" stroke-linejoin="round"/></svg>
      </div>
      <div class="status menu">MENU</div>
    </div>
  </div>

  <div class="control" style="left:335px">
    <div class="label">ENERJİ KESİK</div>
    <svg width="76" height="92" viewBox="0 0 80 96"><circle cx="40" cy="40" r="36" fill="#cfd2e0"/><circle cx="40" cy="40" r="32" fill="var(--knob)"/><rect x="30" y="14" width="20" height="78" rx="9" fill="var(--knob)"/></svg>
  </div>
  <div class="control" style="left:477px">
    <div class="label">ALARM ERTELE</div>
    <svg width="76" height="92" viewBox="0 0 80 96"><circle cx="40" cy="40" r="36" fill="#cfd2e0"/><circle cx="40" cy="40" r="31" fill="#0f7a2e"/><circle cx="40" cy="40" r="26" fill="var(--go-green)"/></svg>
  </div>
  <div class="control" style="left:621px">
    <div class="label">YEDEK ALARM</div>
    <svg width="76" height="92" viewBox="0 0 80 96"><circle cx="40" cy="40" r="34" fill="#cfd2e0"/><circle cx="40" cy="40" r="30" fill="var(--knob)"/><rect x="31" y="16" width="18" height="74" rx="8" fill="var(--knob)"/></svg>
  </div>

  <div class="brand-line"></div>
  <div class="brand">
    <span class="mark"></span>
    <span class="name">TQ27</span>
  </div>
</div>
</body>
</html>
```